Filmproduktion braucht Visitenkarten und Briefpapier
Zielgruppe
Wir sind eine junge Filmproduktion Firma mit dem Namen Lichtkante.
Unser Kerngeschäft sind Image und Unternehmensfilme, sowie Event und Messefilme.
Aufgabenstellung
Wir sind junge, kreative, Filmschaffende und das soll sich auch in der Visitenkarte widerspiegeln, dennoch macht bitte auch ein paar klassische Vorschläge, manchmal ist weniger mehr.
Unser altes Briefpapier ist angehängt. Das neue Briefpapier muss von uns veränderbar sein, da wir noch nicht alle Daten haben wie Steuernummer und USt-ID, bitte aber schon als Dummy anlegen.
Unsere alten Visitenkarten sind angehängt, diese Daten Stimmen, aber ansonsten stimmt daran nix, wie wir finden. Bitte nicht daran Orientieren!!!
Bitte bei der Adresse Lichtkante GbR schreiben.
Unser neues Logo, jetzt in blau ist ebenfalls angehängt.
Viel Spass beim Designen.

```html
<!DOCTYPE html>
<html lang="de">
<head>
<meta charset="utf-8">
<title>Lichtkante – Geschäftsausstattung</title>
<link rel="stylesheet" href="https://fonts.googleapis.com/css2?family=Source+Sans+3:wght@400;600&display=swap">
<style>
  :root {
    --bg: #e6e7e9;
    --paper: #f6f6f7;
    --paper-edge: #d9dadc;
    --blue: #2f7fc1;
    --ink: #1c1c1c;
    --grey-text: #555;
    --shadow: 0 6px 14px rgba(0,0,0,.12);
  }
  * { margin: 0; padding: 0; box-sizing: border-box; }
  html, body { width: 1200px; height: 795px; overflow: hidden; }
  body {
    background: var(--bg);
    font-family: "Source Sans 3", sans-serif;
    color: var(--ink);
    position: relative;
  }
  .sheet {
    position: absolute;
    background: var(--paper);
    box-shadow: var(--shadow);
    border: 1px solid var(--paper-edge);
  }
  .wordmark {
    display: flex;
    align-items: center;
    gap: 7px;
    font-weight: 600;
    text-transform: uppercase;
    letter-spacing: .32em;
    color: var(--ink);
    white-space: nowrap;
  }
  .wordmark .dot {
    width: 9px; height: 9px; border-radius: 50%;
    background: var(--blue); flex: none;
  }
  .wordmark.on-blue { color: #fff; }
  .wordmark.on-blue .dot { background: #fff; }

  /* business cards */
  .card { width: 180px; height: 108px; }
  .card-front { left: 160px; top: 70px; }
  .card-front .wordmark { position: absolute; top: 22px; left: 0; right: 0; justify-content: center; font-size: 10px; }
  .card-front .band {
    position: absolute; left: 0; right: 0; top: 54px; height: 38px;
    background: var(--blue); color: #fff;
    font-size: 6.5px; line-height: 1.35; padding: 6px 12px;
    white-space: nowrap;
  }
  .card-back { left: 160px; top: 200px; background: var(--blue); border-color: #2a72ad; }
  .card-back .wordmark { position: absolute; inset: 0; justify-content: center; font-size: 11px; }

  /* letterhead */
  .letterhead { left: 370px; top: 30px; width: 330px; height: 467px; }
  .letterhead .wordmark { position: absolute; top: 34px; right: 30px; font-size: 10px; }
  .letterhead .sender {
    position: absolute; top: 52px; left: 30px;
    font-size: 5.5px; color: var(--blue); white-space: nowrap;
  }
  .footer-block {
    position: absolute; font-size: 6px; line-height: 1.4; color: var(--grey-text);
    white-space: nowrap;
  }
  .footer-block h4 { color: var(--blue); font-weight: 600; font-size: 6px; }
  .fb-bank { left: 30px; top: 400px; }
  .fb-lead { left: 120px; top: 400px; }
  .fb-contact { left: 220px; top: 400px; }

  /* folder */
  .folder { left: 740px; top: 30px; width: 340px; height: 481px; }
  .folder::before {
    content: ""; position: absolute; left: 8px; top: 0; bottom: 0;
    border-left: 1px solid var(--paper-edge);
  }
  .folder .wordmark { position: absolute; top: 120px; right: 40px; font-size: 12px; }

  /* envelopes */
  .envelope { width: 330px; height: 165px; }
  .envelope-front { left: 370px; top: 560px; }
  .envelope-front .wordmark { position: absolute; right: 28px; bottom: 26px; font-size: 10px; }
  .envelope-back { left: 740px; top: 560px; overflow: hidden; }
  .envelope-back .flap {
    position: absolute; left: 0; right: 0; top: 0; height: 52px;
    border-bottom: 1px solid var(--paper-edge);
    background: #f1f1f2;
  }
</style>
</head>
<body>

  <div class="sheet card card-front">
    <div class="wordmark"><span class="dot"></span>Lichtkante</div>
    <div class="band">
      Ida Sommer | Geschäftsführerin<br>
      Lichtkante GbR | Uferweg 7 | 04109 Leipzig<br>
      mail@lichtkante.example | 0341 / 555 010-0
    </div>
  </div>

  <div class="sheet card card-back">
    <div class="wordmark on-blue"><span class="dot"></span>Lichtkante</div>
  </div>

  <div class="sheet letterhead">
    <div class="wordmark"><span class="dot"></span>Lichtkante</div>
    <p class="sender">Lichtkante GbR | Filmproduktion | Uferweg 7 | 04109 Leipzig</p>
    <div class="footer-block fb-bank">
      <h4>Bankverbindung</h4>
      Auenbank Leipzig<br>IBAN: DE00 1234 5678 90<br>BIC: ABCDEFGH123
    </div>
    <div class="footer-block fb-lead">
      <h4>Geschäftsführer</h4>
      Jonas Berg<br>Lena Vogt<br>Paul Reiter
    </div>
    <div class="footer-block fb-contact">
      <h4>Lichtkante GbR</h4>
      Filmproduktion<br>Uferweg 7, 04109 Leipzig<br>
      Mail: mail@lichtkante.example<br>
      Web: www.lichtkante.example<br>
      Telefon: 0341 / 555 010-0
    </div>
  </div>

  <div class="sheet folder">
    <div class="wordmark"><span class="dot"></span>Lichtkante</div>
  </div>

  <div class="sheet envelope envelope-front">
    <div class="wordmark"><span class="dot"></span>Lichtkante</div>
  </div>

  <div class="sheet envelope envelope-back">
    <div class="flap"></div>
  </div>

</body>
</html>
```